QLindex warden tap - styling

We have a prototyped single page application. The content is in place what we need is restyling to

- make it more user friendly
- modern look and feel
- improve accessibility features
- use our brand guidelines (screen shots attached of the full website)

Prototype is available at http://boardviewapp.examplehost.net/

Target form factor:
Primary - tablet
Secondary - desktop

Target Market(s)

Business users - not financial professionals but people working for big companies who have some limited training in the concepts

Number of Pages Required

1 page

Requirements
Must have
• Touch user interface

```html
<!DOCTYPE html>
<html lang="en">
<head>
<meta charset="utf-8">
<title>QLindex – Flight plan dashboard</title>
<link href="https://fonts.googleapis.com/css2?family=Roboto:wght@300;400;500;700&display=swap" rel="stylesheet">
<style>
  :root {
    --brand-blue: #0b5fb0;
    --brand-magenta: #a3155e;
    --sky-blue: #3ea3dc;
    --page-grey: #e9e9e9;
    --panel-white: #ffffff;
    --text-dark: #333333;
    --text-muted: #9a9a9a;
    --footer-black: #0a0a0a;
  }
  * { box-sizing: border-box; margin: 0; padding: 0; }
  html, body { width: 1200px; height: 938px; overflow: hidden; }
  body {
    position: relative;
    font-family: "Roboto", Arial, sans-serif;
    background: var(--page-grey);
    color: var(--text-dark);
  }
  .site-header {
    position: absolute; left: 0; top: 0; width: 1200px; height: 114px;
    background: var(--brand-blue);
  }
  .brand-name {
    position: absolute; left: 176px; top: 34px;
    font-size: 36px; font-weight: 700; color: #fff; letter-spacing: -1px;
  }
  .main-nav {
    position: absolute; right: 173px; top: 44px;
    display: flex; gap: 22px; list-style: none;
  }
  .main-nav li {
    color: #fff; font-size: 15px; display: flex; align-items: center; gap: 8px;
  }
  .main-nav svg { width: 10px; height: 6px; }
  .kpi-card {
    position: absolute; top: 126px; width: 191px; height: 88px;
    background: var(--panel-white); text-align: center;
    box-shadow: 0 1px 2px rgba(0,0,0,.18);
  }
  .kpi-value { display: block; margin-top: 20px; font-size: 26px; font-weight: 500; }
  .kpi-label { display: block; margin-top: 8px; font-size: 12.5px; }
  .kpi-funding .kpi-value { color: var(--sky-blue); }
  .kpi-change .kpi-value, .kpi-progress .kpi-value { color: var(--brand-magenta); }
  .kpi-change .kpi-label { color: var(--brand-blue); }
  .kpi-progress .kpi-label { color: var(--brand-blue); }
  .kpi-projected .kpi-value { color: var(--brand-blue); }
  .chart-panel {
    position: absolute; left: 173px; top: 231px; width: 856px; height: 446px;
    background: var(--panel-white); box-shadow: 0 1px 3px rgba(0,0,0,.2);
  }
  .chart-title {
    position: absolute; left: 29px; top: 18px; font-size: 22px; font-weight: 400;
  }
  .chart-svg { position: absolute; left: 0; top: 0; width: 856px; height: 446px; }
  .controls-band {
    position: absolute; left: 0; top: 707px; width: 1200px; height: 167px;
    background: var(--panel-white);
  }
  .control-title {
    position: absolute; top: 27px; font-size: 18px; font-weight: 500;
    transform: translateX(-50%); white-space: nowrap;
  }
  .strategy-title { left: 353px; color: var(--brand-blue); }
  .contrib-title { left: 827px; color: var(--brand-magenta); }
  .slider-track {
    position: absolute; top: 81px; width: 400px; height: 6px;
    background: #000; border-radius: 3px;
  }
  .slider-fill { position: absolute; left: 0; top: 0; height: 6px; border-radius: 3px; }
  .slider-knob {
    position: absolute; top: -7px; width: 20px; height: 20px; border-radius: 50%;
    margin-left: -10px;
  }
  .strategy-track { left: 173px; }
  .strategy-track .slider-fill, .strategy-track .slider-knob { background: var(--brand-blue); }
  .contrib-track { left: 627px; }
  .contrib-track .slider-fill, .contrib-track .slider-knob { background: var(--brand-magenta); }
  .slider-label { position: absolute; top: 105px; font-size: 13px; white-space: nowrap; }
  .label-centre { transform: translateX(-50%); }
  .label-end { transform: translateX(-100%); }
  .site-footer {
    position: absolute; left: 0; top: 874px; width: 1200px; height: 64px;
    background: var(--footer-black); color: #fff; font-size: 11px;
  }
  .copyright { position: absolute; left: 600px; top: 26px; transform: translateX(-50%); }
  .page-code { position: absolute; left: 1137px; top: 30px; font-size: 12px; }
</style>
</head>
<body>
  <header class="site-header">
    <div class="brand-name">QLindex</div>
    <ul class="main-nav">
      <li>XYZ Limited <svg viewBox="0 0 10 6"><path d="M1 1l4 4 4-4" stroke="#fff" fill="none" stroke-width="1.3"/></svg></li>
      <li>XYZ Pension Scheme <svg viewBox="0 0 10 6"><path d="M1 1l4 4 4-4" stroke="#fff" fill="none" stroke-width="1.3"/></svg></li>
      <li>Technical Provisions <svg viewBox="0 0 10 6"><path d="M1 1l4 4 4-4" stroke="#fff" fill="none" stroke-width="1.3"/></svg></li>
      <li>October 2014 <svg viewBox="0 0 10 6"><path d="M1 1l4 4 4-4" stroke="#fff" fill="none" stroke-width="1.3"/></svg></li>
    </ul>
  </header>

  <div class="kpi-card kpi-funding" style="left:179px"><span class="kpi-value">91%</span><span class="kpi-label">Funding Level</span></div>
  <div class="kpi-card kpi-change" style="left:399px"><span class="kpi-value">-1.7%</span><span class="kpi-label">Funding level Change</span></div>
  <div class="kpi-card kpi-progress" style="left:618px"><span class="kpi-value">3%</span><span class="kpi-label">Progress aginst Flight Plan</span></div>
  <div class="kpi-card kpi-projected" style="left:837px"><span class="kpi-value">67%</span><span class="kpi-label">10yr Projected funding level</span></div>

  <section class="chart-panel">
    <h2 class="chart-title">Flight plan</h2>
    <svg class="chart-svg" viewBox="0 0 999 520" role="img" aria-label="Flight plan line chart, Monday to Sunday">
      <g stroke="#d0d0d0" stroke-dasharray="3 2" stroke-width="1">
        <line x1="70" y1="107" x2="958" y2="107"/>
        <line x1="70" y1="164" x2="958" y2="164"/>
        <line x1="70" y1="222" x2="958" y2="222"/>
        <line x1="70" y1="337" x2="958" y2="337"/>
        <line x1="70" y1="394" x2="958" y2="394" stroke="#aaa"/>
        <line x1="196" y1="70" x2="196" y2="453"/>
        <line x1="323" y1="70" x2="323" y2="453"/>
        <line x1="449" y1="70" x2="449" y2="453"/>
        <line x1="576" y1="70" x2="576" y2="453"/>
        <line x1="702" y1="70" x2="702" y2="453"/>
        <line x1="830" y1="70" x2="830" y2="453"/>
      </g>
      <line x1="70" y1="279" x2="958" y2="279" stroke="#bbb" stroke-width="3" stroke-dasharray="2 2"/>
      <g fill="#999" font-size="20" font-family="Roboto, sans-serif" text-anchor="middle">
        <text x="35" y="113">60</text><text x="35" y="228">40</text><text x="35" y="344">20</text>
      </g>
      <polygon points="133,453 136,289 199,179 324,235 449,123 577,290 703,233 829,205 894,347 896,453" fill="#a3155e" fill-opacity="0.15"/>
      <polygon points="130,453 130,221 133,221 197,307 321,274 448,165 576,279 702,300 829,221 895,338 896,453" fill="#7f8ec2" fill-opacity="0.5"/>
      <polyline points="136,289 199,179 324,235 449,123 577,290 703,233 829,205 894,347" fill="none" stroke="#a3155e" stroke-width="2"/>
      <polyline points="130,453 130,221 133,221 197,307 321,274 448,165 576,279 702,300 829,221 895,338 896,338 896,453 130,453" fill="none" stroke="#0b5fb0" stroke-width="2"/>
      <g fill="#fff" stroke="#a3155e" stroke-width="3">
        <circle cx="136" cy="289" r="8"/><circle cx="199" cy="179" r="8"/><circle cx="324" cy="235" r="8"/>
        <circle cx="449" cy="123" r="8"/><circle cx="577" cy="290" r="8"/><circle cx="703" cy="233" r="8"/>
        <circle cx="829" cy="205" r="8"/><circle cx="894" cy="347" r="8"/>
      </g>
      <circle cx="449" cy="123" r="3" fill="#a3155e"/>
      <g fill="#fff" stroke="#0b5fb0" stroke-width="3">
        <circle cx="133" cy="221" r="8"/><circle cx="197" cy="307" r="8"/><circle cx="321" cy="274" r="8"/>
        <circle cx="448" cy="165" r="8"/><circle cx="576" cy="279" r="8"/><circle cx="702" cy="300" r="8"/>
        <circle cx="829" cy="221" r="8"/><circle cx="895" cy="338" r="8"/>
      </g>
      <line x1="70" y1="453" x2="958" y2="453" stroke="#ccc" stroke-width="2"/>
      <g stroke="#ccc" stroke-width="2">
        <line x1="71" y1="453" x2="71" y2="461"/><line x1="196" y1="453" x2="196" y2="461"/>
        <line x1="323" y1="453" x2="323" y2="461"/><line x1="449" y1="453" x2="449" y2="461"/>
        <line x1="576" y1="453" x2="576" y2="461"/><line x1="702" y1="453" x2="702" y2="461"/>
        <line x1="830" y1="453" x2="830" y2="461"/><line x1="957" y1="453" x2="957" y2="461"/>
      </g>
      <g fill="#aaa" font-size="16" font-family="Roboto, sans-serif" text-anchor="middle">
        <text x="132" y="488">MON</text><text x="259" y="488">TUE</text><text x="387" y="488">WED</text>
        <text x="512" y="488">THU</text><text x="641" y="488">FRI</text><text x="767" y="488">SAT</text>
        <text x="895" y="488">SUN</text>
      </g>
      <g class="chart-tooltip">
        <rect x="400" y="73" width="98" height="35" rx="2" fill="#a3155e"/>
        <polygon points="443,108 455,108 449,114" fill="#a3155e"/>
        <text x="413" y="96" fill="#fff" font-size="15" font-family="Roboto, sans-serif">50</text>
        <path d="M447 97v-11m-4 4l4-4 4 4" stroke="#fff" stroke-width="2" fill="none"/>
        <text x="456" y="96" fill="#fff" font-size="15" font-family="Roboto, sans-serif">14%</text>
      </g>
    </svg>
  </section>

  <section class="controls-band">
    <h3 class="control-title strategy-title">Investment Strategy</h3>
    <div class="slider-track strategy-track"><div class="slider-fill" style="width:160px"></div><div class="slider-knob" style="left:160px"></div></div>
    <span class="slider-label" style="left:186px">Matching</span>
    <span class="slider-label label-centre" style="left:368px">50% / 50%</span>
    <span class="slider-label label-end" style="left:567px">Growth</span>

    <h3 class="control-title contrib-title">Contributions</h3>
    <div class="slider-track contrib-track"><div class="slider-fill" style="width:161px"></div><div class="slider-knob" style="left:161px"></div></div>
    <span class="slider-label" style="left:640px">£0m</span>
    <span class="slider-label label-centre" style="left:818px">£15.0m</span>
    <span class="slider-label label-end" style="left:1022px">£30m</span>
  </section>

  <footer class="site-footer">
    <span class="copyright">© Copyrights 2014 All Right Reserved.</span>
    <span class="page-code">C6</span>
  </footer>
</body>
</html>
```